Supplement Label and Logo design

We are creating a premium brand nootropics (to improve brain function) supplement and would like a label with a logo designed.
Name: Tallowfen Nootropics
Tag Line: The higher power premium nootropics supplement
Include three bullet points:
Can contribute to:
-Improved Focus, Memory & Mood
-Stress & Anxiety Reduction
-Immune System Support
State on label:-
-Made in the UK and include Union Jack logo
-Vegan
Label Design:
A Tallowfen Nootropics logo
We would like a combination of blue and white colours on the label itself with a gold trim at the top and bottom of the label.
We may need some revisions to the content on the label.
We will need to include a supplement facts section. An example of this is attached.

```html
<!DOCTYPE html>
<html lang="en">
<head>
<meta charset="utf-8">
<title>Tallowfen Nootropics – Supplement Label</title>
<link href="https://fonts.googleapis.com/css2?family=Oswald:wght@600&family=Roboto+Condensed:wght@300;400&display=swap" rel="stylesheet">
<style>
  :root {
    --backdrop: #c4c4c4;
    --label-white: #ffffff;
    --navy: #0d1646;
    --gold: #d6a02b;
    --gold-deep: #c58d1c;
    --flag-blue: #1f2f7a;
    --flag-red: #c8202f;
  }
  * { margin: 0; padding: 0; box-sizing: border-box; }
  html, body {
    width: 1200px; height: 800px; overflow: hidden;
    background: var(--backdrop);
    font-family: "Roboto Condensed", "Arial Narrow", sans-serif;
  }
  .label {
    position: absolute;
    left: 290px; top: 80px;
    width: 620px; height: 640px;
    background: var(--label-white);
    border-top: 2px solid var(--gold);
    border-bottom: 2px solid var(--gold);
    text-align: center;
    color: var(--navy);
    overflow: hidden;
  }
  .brand-name {
    position: absolute; left: 50%; top: 52px;
    font-family: "Oswald", "Arial Narrow", sans-serif;
    font-weight: 600; font-size: 84px; letter-spacing: -1px;
    line-height: 1;
    white-space: nowrap;
    transform: translateX(-50%) scaleX(0.72);
    transform-origin: center;
  }
  .tagline {
    position: absolute; left: 53px; right: 68px; top: 155px;
    height: 33px; line-height: 33px;
    background: var(--gold);
    color: var(--label-white);
    font-weight: 400; font-size: 22px; letter-spacing: -0.4px;
    white-space: nowrap;
  }
  .brand-mark {
    position: absolute; left: 236px; top: 208px;
    width: 148px; height: 148px;
    border-radius: 50%;
    background: var(--gold);
  }
  .benefits {
    position: absolute; left: 0; right: 0; top: 424px;
  }
  .benefits-intro {
    color: var(--gold-deep); font-weight: 300; font-size: 19px;
    line-height: 26px;
  }
  .benefits-list { list-style: none; }
  .benefits-list li {
    font-weight: 400; font-size: 21px; line-height: 28px;
    letter-spacing: -0.3px;
  }
  .origin {
    position: absolute; left: 0; right: 0; top: 586px;
    display: flex; justify-content: center; align-items: center; gap: 4px;
    color: var(--gold-deep); font-weight: 300; font-size: 19px;
  }
  .origin svg { width: 38px; height: 20px; }
</style>
</head>
<body>
  <main class="label">
    <h1 class="brand-name">Tallowfen Nootropics</h1>
    <p class="tagline">The higher power premium nootropics supplement</p>
    <div class="brand-mark" aria-hidden="true"></div>
    <section class="benefits">
      <p class="benefits-intro">Can contribute to:</p>
      <ul class="benefits-list">
        <li>Improved Focus, Memory &amp; Mood</li>
        <li>Stress &amp; Anxiety Reduction</li>
        <li>Immune System Support</li>
      </ul>
    </section>
    <p class="origin">Made in the UK
      <svg viewBox="0 0 60 30" aria-label="UK flag">
        <rect width="60" height="30" fill="var(--flag-blue)"/>
        <path d="M0,0 L60,30 M60,0 L0,30" stroke="#fff" stroke-width="6"/>
        <path d="M0,0 L60,30 M60,0 L0,30" stroke="var(--flag-red)" stroke-width="2"/>
        <path d="M30,0 V30 M0,15 H60" stroke="#fff" stroke-width="10"/>
        <path d="M30,0 V30 M0,15 H60" stroke="var(--flag-red)" stroke-width="6"/>
      </svg>
    </p>
  </main>
</body>
</html>
```